VeLT Record Shredding professional postcard

I'm looking for a postcard design that tells a story in very few words about how important it is to protect yourself your family and your clients against sensitive information and identity theft. My website is veltrecordshredding.net if you are looking for text to put on card. Would like "secure and certified destruction of your data and media" on the postcard.

Target Market(s)

Commercial and residential.

Industry/Entity Type

Business Service

Font styles to use
Serif

Colors
000000

Requirements
Must have
• A pic, 1-855-318-4096 phone number, veltrecordshredding.net web address area for postage must be double sided. Definitely want it eye catching. Must have an area for postage and mailing address. Would like to see glossy on one side and the other side not glossy

```html
<!DOCTYPE html>
<html lang="en">
<head>
<meta charset="utf-8">
<title>VeLT Record Shredding – Postcard</title>
<link href="https://fonts.googleapis.com/css2?family=Oswald:wght@300;400;600&family=Montserrat:wght@500;600&display=swap" rel="stylesheet">
<style>
  :root {
    --ink: #000000;
    --night: #0b141b;
    --night-mid: #1d2c36;
    --slate: #3a3a3a;
    --mist: #e1e1e1;
    --paper: #ffffff;
    --green: #8dc63f;
    --green-deep: #6a9a2e;
    --green-dark: #2f3d1c;
    --navy: #1f4e8c;
    --line: #555555;
    --backdrop: #e9e7e4;
  }
  * { box-sizing: border-box; margin: 0; padding: 0; }
  html, body { width: 841px; height: 1200px; overflow: hidden; }
  body { background: var(--backdrop); position: relative; font-family: "Montserrat", sans-serif; }

  .card { position: absolute; left: 74px; width: 685px; background: var(--paper); box-shadow: 0 3px 10px rgba(0,0,0,.25); overflow: hidden; }

  /* Front */
  .card--front { top: 66px; height: 440px; }
  .front-hero { position: absolute; left: 0; top: 0; width: 685px; height: 374px;
    background: radial-gradient(ellipse at 55% 35%, #5c6b75 0%, var(--night-mid) 35%, var(--night) 75%); }
  .front-headline-band { position: absolute; left: 0; top: 203px; width: 635px; height: 171px; background: rgba(0,0,0,.72); }
  .front-headline { position: absolute; left: 21px; top: 212px; font-family: "Oswald", sans-serif; font-weight: 600;
    font-size: 44px; line-height: 47px; color: var(--paper); letter-spacing: -0.5px; text-transform: uppercase; }
  .front-headline .accent { color: var(--green); }
  .front-tiles { position: absolute; left: 635px; top: 203px; width: 50px; height: 171px; }
  .front-footer { position: absolute; left: 0; top: 374px; width: 685px; height: 66px; }
  .brand { font-family: "Montserrat", sans-serif; font-weight: 600; color: var(--navy); display: flex; align-items: center; gap: 6px; }
  .brand-dot { width: 12px; height: 12px; border-radius: 50%; background: var(--green); flex: none; }
  .front-footer .brand { position: absolute; left: 18px; top: 22px; font-size: 12px; }
  .front-contact { position: absolute; right: 14px; top: 18px; text-align: right; font-size: 12.5px; line-height: 18px; color: var(--ink); font-weight: 500; }

  /* Back */
  .card--back { top: 663px; height: 441px; }
  .back-panel { position: absolute; left: 0; top: 0; width: 347px; height: 357px; background: var(--slate); }
  .back-photo { position: absolute; left: 23px; top: 23px; width: 299px; height: 169px; border: 4px solid #d8d8d8;
    background: linear-gradient(100deg, #3a2f2f 0%, #e9e4e4 25%, #f3eeee 60%, #c98f8f 100%); }
  .mission-title { position: absolute; left: 23px; top: 205px; font-family: "Oswald", sans-serif; font-weight: 400;
    font-size: 17px; color: var(--paper); }
  .mission-text { position: absolute; left: 23px; top: 236px; width: 299px; font-family: "Oswald", sans-serif; font-weight: 300;
    font-size: 10.6px; line-height: 13.4px; color: var(--paper); text-align: justify; }
  .back-footer { position: absolute; left: 0; top: 357px; width: 347px; height: 84px; background: var(--mist); }
  .back-footer-text { position: absolute; left: 23px; top: 14px; font-family: "Oswald", sans-serif; font-weight: 300;
    font-size: 12px; line-height: 20px; color: var(--ink); }
  .back-footer-text strong { font-weight: 400; font-size: 13px; }
  .badges { position: absolute; left: 247px; top: 28px; display: flex; gap: 5px; }
  .badge { width: 39px; height: 39px; border-radius: 50%; }
  .badge--teal { background: #1c6a63; }
  .badge--blue { background: #1e5f8a; border: 3px solid #ffffff; box-shadow: 0 0 0 1px #1e5f8a; }
  .back-address { position: absolute; left: 347px; top: 0; width: 338px; height: 441px; }
  .back-address .brand { position: absolute; left: 36px; top: 50px; font-size: 12px; }
  .stamp-box { position: absolute; left: 244px; top: 30px; width: 70px; height: 69px; border: 1px solid var(--line); }
  .address-line { position: absolute; left: 84px; width: 230px; height: 0; border-top: 1px solid var(--line); }
</style>
</head>
<body>

<section class="card card--front">
  <div class="front-hero" role="img" aria-label="Hard drive disintegrating into fragments against a dark background"></div>
  <div class="front-headline-band"></div>
  <h1 class="front-headline">Certified and secure<br><span class="accent">complete destruction</span><br>of data and media</h1>
  <svg class="front-tiles" viewBox="0 0 50 171" aria-hidden="true">
    <rect x="0" y="0" width="50" height="171" fill="var(--green)"/>
    <rect x="0" y="0" width="15" height="171" fill="var(--green-deep)"/>
    <rect x="0" y="57" width="50" height="57" fill="var(--green-deep)"/>
    <rect x="0" y="57" width="15" height="57" fill="var(--green-dark)"/>
  </svg>
  <div class="front-footer">
    <div class="brand"><span class="brand-dot"></span>VeLT Record Shredding</div>
    <p class="front-contact">Serving Long Island and the Tri State Area<br>call us at 1-855-318-4096</p>
  </div>
</section>

<section class="card card--back">
  <div class="back-panel">
    <div class="back-photo" role="img" aria-label="Mobile shredding trailer parked at night"></div>
    <h2 class="mission-title">Our Mission</h2>
    <p class="mission-text">The security of your sensitive data is paramount to us. As a result, our primary goal is to assure the most secure and complete destruction of your data and electronic media to an irretrievable state. Our mobile destruction van visits client sites and using the onboard state-of-the-art shredders destroys data media. Clients are assured that their data is controlled and confidentially handled from receipt to destruction in our shredder. Not only is this more efficient for our clients, they can be assured the data is destroyed before the media leaves their property.</p>
  </div>
  <div class="back-footer">
    <p class="back-footer-text"><strong>Serving Long Island and the Tri State Area</strong><br>call us at <strong>1-855-318-4096</strong><br>or visit <strong>veltrecordshredding.net</strong></p>
    <div class="badges">
      <span class="badge badge--teal"></span>
      <span class="badge badge--blue"></span>
    </div>
  </div>
  <div class="back-address">
    <div class="brand"><span class="brand-dot"></span>VeLT Record Shredding</div>
    <div class="stamp-box"></div>
    <div class="address-line" style="top:180px"></div>
    <div class="address-line" style="top:207px"></div>
    <div class="address-line" style="top:234px"></div>
    <div class="address-line" style="top:262px"></div>
  </div>
</section>

</body>
</html>
```